Webdesign for Property Renting Business

We need a professional and slim design for a hight quality property renting website which is not overcrowded with too much information and has a clear and easily structure to read. The visitor should get an instant impression what he can do at a glance.

The goal of this contest is to get a design for building a prototype of the website and to attract our client and owner of the site by a good looking prototype and not just a wireframe. Therefore we don't need an HTML-coded design at this early project-stage. We only expect getting a simple bitmap or vector-graphic design.

Actually we don't have a logo. Use a placeholder or feel free to design a simple one by yourself.

Last but not least if you have a good idea just include it in to your design.

Our goal is to get a design for building a prototype of the website and to attract our client by a good looking prototype and not just a wireframe.

Target Market(s)

People who want to spend money to rent a good quality property. Not only the riches. These could be business people and also demanding families as well.

Industry/Entity Type

Building

Colors
85cae6

Requirements
Must have
• We need two sites, a start site and a property-details site. Each site has to include the following points:

1.) start site
- search mask (location, date to choose, quanity of guests)
- show some properties (highlights, special offers etc.)
- show login/register link

2.) property site
- Location in Vorlen Map
- Photos, Description, Amenities, Calendar (available,not available), Contact, Reviews

These are some sites which I like from a design prospective
- http://www.stayquelo.com
- http://www.lodvanta.com/
- http://www.dwellirox.com/
- http://www.plomavi.com

These are some sites which I dislike:
1.) http://www.gallic-estatio.com/guides/france/rent/
2.) http://www.solohomvenu.co.za/property-rentals.htm

We don't need an HTML-coded design at this early project-stage. We only expect getting a simple bitmap or vector-graphic design. Maybe with the PSD-file (or wathever program you use) that we can pick-out some elements for building the prototype.

```html
<!DOCTYPE html>
<html lang="en">
<head>
<meta charset="utf-8">
<title>Roomvela – Property Renting</title>
<link href="https://fonts.googleapis.com/css2?family=Gelasio:wght@400;700&family=Open+Sans:wght@400;600&display=swap" rel="stylesheet">
<style>
:root{
  --cyan:#1fc8db;
  --cyan-dark:#15a9bb;
  --dark:#3b3b3b;
  --text:#333;
  --muted:#555;
  --line:#9a9a9a;
  --footer-bg:#f2f2f2;
  --white:#fff;
}
*{margin:0;padding:0;box-sizing:border-box}
html,body{width:1200px;height:2200px;overflow:hidden;background:var(--white)}
.page{position:relative;width:1200px;height:2200px;overflow:hidden;font-family:'Open Sans',sans-serif;color:var(--text)}
.serif{font-family:'Gelasio',serif}
.abs{position:absolute}

/* header */
.brand{left:158px;top:18px;display:flex;align-items:center;gap:10px}
.brand-mark{width:26px;height:26px;border-radius:50%;background:var(--cyan)}
.brand-name{font-family:'Gelasio',serif;font-size:22px;color:var(--text)}
.nav{left:305px;top:32px;display:flex;gap:24px;font-family:'Gelasio',serif;font-size:16px}
.nav a{color:var(--text);text-decoration:none}
.nav a.active{color:var(--cyan)}
.btn{display:flex;align-items:center;justify-content:center;font-family:'Gelasio',serif;color:var(--white);text-decoration:none}
.btn-login{left:882px;top:23px;width:89px;height:34px;background:var(--cyan-dark);font-size:16px}
.btn-register{left:987px;top:23px;width:90px;height:34px;background:#4a4a4a;font-size:16px}

/* hero */
.hero{left:0;top:78px;width:1200px;height:581px;background:linear-gradient(180deg,#e9eef2 0%,#d6dde0 40%,#b9c4b3 75%,#6f8f4d 100%)}
.hero-arrow{top:300px}
.search{left:166px;top:524px;width:868px;height:110px;background:rgba(255,255,255,.85)}
.field{top:28px;height:58px;background:var(--white);border:1px solid #ddd;display:flex;align-items:center;font-family:'Gelasio',serif;font-size:16px;color:#444}
.field svg.icon{margin:0 10px 0 14px}
.field .drop{position:absolute;right:8px;top:15px;width:28px;height:28px;background:var(--cyan);display:flex;align-items:center;justify-content:center}
.go{left:774px;top:28px;width:74px;height:58px;background:var(--cyan);color:var(--white);font-weight:700;font-size:22px;font-family:'Open Sans',sans-serif;display:flex;align-items:center;justify-content:center;letter-spacing:1px}

/* sections */
.section-title{width:1200px;text-align:center;font-family:'Gelasio',serif;font-size:28px;color:#444}
.rule{left:166px;width:868px;height:1px;background:var(--line)}
.photo{width:276px;height:172px}
.card-title{font-family:'Gelasio',serif;font-size:22px;color:var(--cyan)}
.card-info{font-size:13px;line-height:22px;color:var(--muted)}
.btn-cyan{background:var(--cyan);font-size:15px;width:106px;height:33px}
.btn-more{left:525px;top:1482px;width:150px;height:44px;background:var(--dark);font-size:16px}

.offer{width:276px;height:172px}
.offer-photo{position:absolute;left:0;top:0;width:276px;height:118px}
.badge{position:absolute;right:10px;top:6px;width:47px;height:80px;background:var(--dark);color:var(--white);font-family:'Open Sans',sans-serif;font-weight:600;font-size:15px;line-height:16px;text-align:center;padding-top:12px}
.badge small{font-size:11px;display:block;line-height:13px}
.offer-band{position:absolute;left:0;top:118px;width:276px;height:54px;background:var(--cyan);color:var(--white);font-family:'Gelasio',serif;display:flex;align-items:center;justify-content:space-between;padding:0 10px}
.offer-band .label{font-size:16px}
.offer-band .price{font-size:20px}
.btn-offer{width:95px;height:37px;background:var(--cyan);font-size:13px}

/* footer */
.footer{left:0;top:1879px;width:1200px;height:321px;background:var(--footer-bg)}
.foot-col h4{font-weight:400;font-size:16px;color:#444;margin-bottom:24px}
.foot-col li{list-style:none;font-size:12px;line-height:28px;color:#444}
.newsletter p{font-size:12px;line-height:19px;color:#444;width:200px}
.input{width:204px;height:26px;background:var(--white);font-size:9px;color:#aaa;padding:7px;margin-top:12px}
.btn-sub{width:77px;height:26px;background:var(--cyan);font-size:13px;font-weight:600;font-family:'Open Sans',sans-serif;margin:10px 0 0 127px}
.social li{display:flex;justify-content:space-between;align-items:center;width:130px;line-height:34px}
.dot{width:25px;height:25px;border-radius:50%;background:var(--cyan)}
.copyright{top:2158px;width:1200px;text-align:center;font-size:12px;color:#444}
</style>
</head>
<body>
<div class="page">

  <header>
    <div class="abs brand"><span class="brand-mark"></span><span class="brand-name">Roomvela</span></div>
    <nav class="abs nav">
      <a class="active" href="#">Home</a><a href="#">About Us</a><a href="#">Renting Properties</a><a href="#">Offers</a><a href="#">FAQ's</a><a href="#">Contact Us</a>
    </nav>
    <a class="abs btn btn-login" href="#">Login</a>
    <a class="abs btn btn-register" href="#">Register</a>
  </header>

  <section class="abs hero" role="img" aria-label="Smiling couple standing in front of a white family house with a garden">
    <svg class="abs hero-arrow" style="left:116px" width="40" height="68" viewBox="0 0 40 68"><path d="M34 4 L6 34 L34 64" fill="none" stroke="#7d7d7d" stroke-width="8"/></svg>
    <svg class="abs hero-arrow" style="left:1040px" width="40" height="68" viewBox="0 0 40 68"><path d="M6 4 L34 34 L6 64" fill="none" stroke="#7d7d7d" stroke-width="8"/></svg>
  </section>

  <form class="abs search">
    <div class="abs field" style="left:20px;width:220px">
      <svg class="icon" width="14" height="20" viewBox="0 0 14 20"><path d="M7 0a7 7 0 0 0-7 7c0 5 7 13 7 13s7-8 7-13a7 7 0 0 0-7-7zm0 10a3 3 0 1 1 0-6 3 3 0 0 1 0 6z" fill="#444"/></svg>Location
      <span class="drop"><svg width="12" height="8" viewBox="0 0 12 8"><path d="M1 1l5 5 5-5" stroke="#fff" stroke-width="2" fill="none"/></svg></span>
    </div>
    <div class="abs field" style="left:254px;width:249px">
      <svg class="icon" width="18" height="20" viewBox="0 0 18 20"><rect x="1" y="3" width="16" height="16" fill="none" stroke="#444" stroke-width="2"/><rect x="1" y="3" width="16" height="4" fill="#444"/><rect x="4" y="0" width="2" height="5" fill="#444"/><rect x="12" y="0" width="2" height="5" fill="#444"/><path d="M4 10h2v2H4zm4 0h2v2H8zm4 0h2v2h-2zM4 14h2v2H4zm4 0h2v2H8zm4 0h2v2h-2z" fill="#444"/></svg>Date To Choose
      <span class="drop"><svg width="12" height="8" viewBox="0 0 12 8"><path d="M1 1l5 5 5-5" stroke="#fff" stroke-width="2" fill="none"/></svg></span>
    </div>
    <div class="abs field" style="left:516px;width:247px">
      <svg class="icon" width="18" height="18" viewBox="0 0 18 18"><circle cx="9" cy="5" r="4.5" fill="#444"/><path d="M0 18c0-5 4-7 9-7s9 2 9 7z" fill="#444"/></svg>Quantity Of Guests
      <span class="drop"><svg width="12" height="8" viewBox="0 0 12 8"><path d="M1 1l5 5 5-5" stroke="#fff" stroke-width="2" fill="none"/></svg></span>
    </div>
    <div class="abs go">GO</div>
  </form>

  <h2 class="abs section-title" style="left:0;top:700px">Property Highlights</h2>
  <div class="abs rule" style="top:752px"></div>

  <!-- highlights row 1 -->
  <div class="abs photo" style="left:166px;top:761px;background:linear-gradient(180deg,#3f7fd0,#9ac0ec 55%,#6b4a35 80%,#4a3a2a)" role="img" aria-label="Brick house with a damaged roof under a blue sky"></div>
  <div class="abs photo" style="left:461px;top:761px;background:linear-gradient(180deg,#0d1d4a,#22407a 45%,#c6b08a 65%,#2d5d3a 85%,#1a6a9a)" role="img" aria-label="Luxury villa at dusk with lit windows and a pool"></div>
  <div class="abs photo" style="left:757px;top:761px;background:linear-gradient(180deg,#9bbde0,#d8c6a8 40%,#6a7c82 70%,#9a8a70)" role="img" aria-label="Desert home with a rocky pool and cactus garden"></div>

  <div class="abs" style="left:161px;top:944px"><h3 class="card-title">Coral Haven</h3><p class="card-info">2 BHK Apts,<br>Rs. 51.42 Lacs Onwards<br>Pallikaranai,Chennai</p></div>
  <div class="abs" style="left:459px;top:944px"><h3 class="card-title">Coral Haven</h3><p class="card-info">2 BHK Apts,<br>Rs. 51.42 Lacs Onwards<br>Pallikaranai,Chennai</p></div>
  <div class="abs" style="left:757px;top:944px"><h3 class="card-title">Coral Haven</h3><p class="card-info">2 BHK Apts,<br>Rs. 51.42 Lacs Onwards<br>Pallikaranai,Chennai</p></div>
  <a class="abs btn btn-cyan" style="left:161px;top:1045px" href="#">View Details</a>
  <a class="abs btn btn-cyan" style="left:461px;top:1045px" href="#">View Details</a>
  <a class="abs btn btn-cyan" style="left:757px;top:1045px" href="#">View Details</a>

  <!-- highlights row 2 -->
  <div class="abs photo" style="left:166px;top:1116px;background:linear-gradient(180deg,#4a8ed8,#b8d2ee 35%,#8a4a3a 55%,#9a9a8a 75%,#5a8a3a)" role="img" aria-label="Red brick house with a gravel driveway and lawn"></div>
  <div class="abs photo" style="left:463px;top:1116px;background:linear-gradient(180deg,#d8d8d8,#a8604a 35%,#c4a890 60%,#8a6a5a)" role="img" aria-label="Mediterranean villa with arched windows and palm trees"></div>
  <div class="abs photo" style="left:757px;top:1116px;background:linear-gradient(180deg,#5a7ab8,#9ab0d0 40%,#3a6a9a 65%,#1a3a5a)" role="img" aria-label="Infinity pool at a modern seaside home at sunset"></div>

  <div class="abs" style="left:161px;top:1302px"><h3 class="card-title">Coral Haven</h3><p class="card-info">2 BHK Apts,<br>Rs. 51.42 Lacs Onwards<br>Pallikaranai,Chennai</p></div>
  <div class="abs" style="left:459px;top:1302px"><h3 class="card-title">Coral Haven</h3><p class="card-info">2 BHK Apts,<br>Rs. 51.42 Lacs Onwards<br>Pallikaranai,Chennai</p></div>
  <div class="abs" style="left:757px;top:1302px"><h3 class="card-title">Coral Haven</h3><p class="card-info">2 BHK Apts,<br>Rs. 51.42 Lacs Onwards<br>Pallikaranai,Chennai</p></div>
  <a class="abs btn btn-cyan" style="left:161px;top:1405px" href="#">View Details</a>
  <a class="abs btn btn-cyan" style="left:461px;top:1405px" href="#">View Details</a>
  <a class="abs btn btn-cyan" style="left:757px;top:1405px" href="#">View Details</a>

  <div class="abs rule" style="top:1482px"></div>
  <a class="abs btn btn-more" href="#">More Properties</a>

  <h2 class="abs section-title" style="left:0;top:1548px">Latest Offers</h2>
  <div class="abs rule" style="top:1589px"></div>

  <div class="abs offer" style="left:166px;top:1606px">
    <div class="offer-photo" style="background:linear-gradient(180deg,#2a4a8a,#8aa8d0 50%,#c8ccd0)" role="img" aria-label="Modern high-rise apartment buildings"></div>
    <div class="badge">25%<small>SALE<br>OFFER</small></div>
    <div class="offer-band"><span class="label">Offer Price</span><span class="price">$ 2930020.00</span></div>
  </div>
  <div class="abs offer" style="left:463px;top:1606px">
    <div class="offer-photo" style="background:linear-gradient(180deg,#2a5a9a,#8ab0d8 50%,#d0d4d8 80%,#4a6a3a)" role="img" aria-label="White apartment block with palm trees"></div>
    <div class="badge">25%<small>SALE<br>OFFER</small></div>
    <div class="offer-band"><span class="label">Offer Price</span><span class="price">$ 2930020.00</span></div>
  </div>
  <div class="abs offer" style="left:757px;top:1606px">
    <div class="offer-photo" style="background:linear-gradient(180deg,#3a6ab0,#9ab8e0 45%,#8a7a6a 70%,#6a6a5a)" role="img" aria-label="Suburban house with garage"></div>
    <div class="badge">25%<small>SALE<br>OFFER</small></div>
    <div class="offer-band"><span class="label">Offer Price</span><span class="price">$ 2930020.00</span></div>
  </div>
  <a class="abs btn btn-offer" style="left:164px;top:1787px" href="#">View Details</a>
  <a class="abs btn btn-offer" style="left:463px;top:1787px" href="#">View Details</a>
  <a class="abs btn btn-offer" style="left:757px;top:1787px" href="#">View Details</a>

  <footer class="abs footer">
    <div class="abs foot-col" style="left:161px;top:32px">
      <h4>Quick Links</h4>
      <ul><li>Home</li><li>About Us</li><li>Renting Properties</li><li>Offers</li><li>FAQ's</li><li>Contact Us</li></ul>
    </div>
    <div class="abs foot-col" style="left:384px;top:32px">
      <h4>Support Links</h4>
      <ul><li>Legal Notice</li><li>Privacy Policy</li><li>Terms &amp; Conditions</li><li>Help</li></ul>
    </div>
    <div class="abs foot-col newsletter" style="left:607px;top:32px">
      <h4 style="margin-bottom:14px">Newsletter SignUp</h4>
      <p>Sign-up for our daily emails by entering your information below:</p>
      <div class="input">Name</div>
      <div class="input">Enter Your E-Mail ID</div>
      <div class="btn btn-sub">Subscribe</div>
    </div>
    <div class="abs foot-col social" style="left:902px;top:32px">
      <h4 style="margin-bottom:14px">Connect With Us</h4>
      <ul><li>Chirpnet<span class="dot"></span></li><li>Friendora<span class="dot"></span></li><li>Workmesh<span class="dot"></span></li></ul>
    </div>
  </footer>
  <p class="abs copyright" style="left:0">Copyright ©2013 Company Name &nbsp;- All rights reserved</p>
</div>
</body>
</html>
```